"Tales of Quiet Harbors" Book Cover Design

I am seeking a dynamic, modern, and professional cover design for a book focused on groundbreaking science that explores how a supplement called plasmalogens can revitalize the brain, prevent Alzheimer’s, and safeguard memories. The design should strike a balance between being visually appealing and conveying the seriousness of the topic.

Target Market(s)

The target audience includes individuals who are curious about cutting-edge science and proactive approaches to brain health, as well as those seeking to better understand how to protect their cognitive functions and memories. The cover should resonate with readers interested in health, science, and self-improvement, while reflecting the book’s informative and empowering tone.

Requirements
Must have
• The quotation across the top of the page (this is a placeholder for now, it will be changed eventually) and the author's name.
Should not have
• You don't need to use the puzzle idea!

```html
<!DOCTYPE html>
<html lang="en">
<head>
<meta charset="utf-8">
<title>Tales of Quiet Harbors — Book Cover</title>
<link href="https://fonts.googleapis.com/css2?family=Montserrat:wght@200;300;400;500&display=swap" rel="stylesheet">
<style>
  :root {
    --cover-green: #27ad78;
    --cover-teal: #2aa89a;
    --glow-blue: #21a3d6;
    --ink-white: #ffffff;
    --rule-white: rgba(255, 255, 255, 0.85);
  }
  html, body {
    margin: 0;
    padding: 0;
    overflow: hidden;
    background: var(--cover-green);
  }
  .cover {
    position: relative;
    width: 927px;
    height: 1200px;
    overflow: hidden;
    font-family: "Montserrat", sans-serif;
    color: var(--ink-white);
    background:
      radial-gradient(circle at 450px 600px, var(--glow-blue) 0%, var(--cover-teal) 38%, var(--cover-green) 70%);
  }
  .pattern-layer {
    position: absolute;
    inset: 0;
    background: radial-gradient(circle at 50% 50%, rgba(20, 120, 90, 0.06), rgba(20, 120, 90, 0.1));
  }
  .endorsement {
    position: absolute;
    top: 54px;
    left: 0;
    width: 100%;
    text-align: center;
    font-size: 20px;
    line-height: 26px;
  }
  .endorsement__quote { font-weight: 300; margin: 0; }
  .endorsement__source { font-weight: 500; margin: 0; }

  .title-top {
    position: absolute;
    top: 204px;
    left: 0;
    width: 100%;
    text-align: center;
    font-weight: 300;
    font-size: 88px;
    line-height: 1;
    letter-spacing: 2px;
    margin: 0;
  }
  .rule {
    position: absolute;
    left: 233px;
    width: 461px;
    height: 1px;
    background: linear-gradient(90deg, transparent, var(--rule-white) 15%, var(--rule-white) 85%, transparent);
  }
  .rule--upper { top: 348px; }
  .rule--lower { top: 800px; }

  .title-scatter {
    position: absolute;
    inset: 0;
    margin: 0;
    font-weight: 300;
    font-size: 122px;
    line-height: 1;
  }
  .scatter-letter {
    position: absolute;
    display: block;
  }
  .scatter-letter--q { left: 150px; top: 540px; }
  .scatter-letter--u { left: 262px; top: 432px; transform: rotate(-15deg); }
  .scatter-letter--i { left: 528px; top: 406px; transform: rotate(22deg); }
  .scatter-letter--e { left: 608px; top: 432px; transform: rotate(12deg); }
  .scatter-letter--t { left: 694px; top: 562px; }

  .brain-art {
    position: absolute;
    left: 365px;
    top: 445px;
    width: 170px;
    height: 300px;
    border-radius: 85px 85px 60px 60px;
    background: linear-gradient(180deg, rgba(255, 255, 255, 0.35) 0%, rgba(255, 255, 255, 0.12) 55%, rgba(255, 255, 255, 0) 100%);
  }

  .title-bottom {
    position: absolute;
    top: 852px;
    left: 0;
    width: 100%;
    text-align: center;
    font-weight: 300;
    font-size: 112px;
    line-height: 1;
    margin: 0;
  }
  .author {
    position: absolute;
    top: 1066px;
    left: 0;
    width: 100%;
    text-align: center;
    font-weight: 500;
    font-size: 22px;
    letter-spacing: 13px;
    margin: 0;
  }
</style>
</head>
<body>
  <main class="cover">
    <div class="pattern-layer" role="img" aria-label="Faint organic squiggle pattern across the green background"></div>

    <header class="endorsement">
      <p class="endorsement__quote">“An Incredible guide to protecting your mind and memories.”</p>
      <p class="endorsement__source">- Dr Lena Hartwell, MD</p>
    </header>

    <h1 class="title-top">TALES OF</h1>
    <div class="rule rule--upper"></div>

    <p class="title-scatter" aria-label="Quiet">
      <span class="scatter-letter scatter-letter--q">Q</span>
      <span class="scatter-letter scatter-letter--u">U</span>
      <span class="scatter-letter scatter-letter--i">I</span>
      <span class="scatter-letter scatter-letter--e">E</span>
      <span class="scatter-letter scatter-letter--t">T</span>
    </p>
    <div class="brain-art" role="img" aria-label="Line-drawn brain breaking apart into falling fragments"></div>

    <div class="rule rule--lower"></div>
    <p class="title-bottom">HARBORS</p>

    <p class="author">MARTIN ELLERY, MD</p>
  </main>
</body>
</html>
```